IT Services

We come to you
Only $49/hr
No contract, no monthly fee
Software engineer on staff
remote assistance or visit in your office

On the back of the card I want to list services.

- Server setup
- Network troubleshooting
- Printer setup
- Secure backup setup
- Software installation
- Wireless network setup
- Wired network setup
- Disaster recovery
- Website management
- Any other technology related support
- Email setup
- HIPAA compliance review and setup
Updates

the URL is: GEARFIXPRO.ZONE please use it on the card

On the card we need to mention "Connect remotely to address your IT issues" if there is enough room as well as "we go to you"

Industry/Entity Type

Printer

Contact Information for Business Card

I want a busoiness card to offer my services to doctor offices, it can be dentists, Otamatry, and other professions. I provide the following service. My plan is to go to their office and drop off my card. I don't want them to forget about it that is why I am paying for the design. I like hand writing design formats.

```html
<!DOCTYPE html>
<html lang="en">
<head>
<meta charset="utf-8">
<title>GEARFIXPRO.ZONE – Business Cards</title>
<link rel="stylesheet" href="https://fonts.googleapis.com/css2?family=Architects+Daughter&family=Cabin:wght@400;500&family=Roboto+Condensed:wght@300;400;700&display=swap">
<style>
  :root {
    --backdrop: #e4e5e7;
    --paper: #ffffff;
    --orange: #e8802c;
    --orange-soft: #e69a63;
    --ink: #5b5b5b;
    --slate: #565657;
    --mist: #a2a2a2;
    --black: #111111;
  }
  html, body {
    margin: 0;
    width: 1200px;
    height: 794px;
    overflow: hidden;
    background: var(--backdrop);
  }
  .canvas { position: relative; width: 1200px; height: 794px; }
  .card { position: absolute; display: block; }
  .card--front-plain   { left: 33px;  top: 36px;  }
  .card--front-skyline { left: 619px; top: 36px;  }
  .card--back          { left: 617px; top: 437px; }

  .hand { font-family: "Architects Daughter", cursive; }
  .perk { font-size: 13px; letter-spacing: 0.4px; }
  .perk--accent { fill: var(--orange); }
  .perk--plain  { fill: var(--ink); }
  .skyline .perk--plain { fill: var(--mist); }
  .skyline-block { fill: var(--slate); }

  .wordmark { font-family: "Architects Daughter", cursive; font-size: 28px; fill: var(--ink); }
  .wordmark--back { fill: #c4c4c4; }

  .contact-name { font-family: "Cabin", sans-serif; font-size: 16px; font-weight: 500; fill: var(--ink); }
  .contact-line { font-family: "Cabin", sans-serif; font-size: 12.5px; fill: var(--ink); }

  .service { font-family: "Roboto Condensed", sans-serif; }
  .service--wide    { font-size: 17px; font-weight: 400; fill: var(--mist); letter-spacing: 0.6px; }
  .service--orange  { font-weight: 700; fill: var(--orange); }
  .service--light   { font-weight: 300; fill: var(--orange-soft); font-size: 12.5px; }
  .service--black   { font-weight: 400; fill: var(--black); font-size: 13px; }
  .service--blackb  { font-weight: 700; fill: var(--black); font-size: 14px; }
  .service--grey    { font-weight: 700; fill: var(--mist); font-size: 14px; }
  .service--greythin{ font-weight: 300; fill: var(--mist); font-size: 11.5px; }
</style>
</head>
<body>
<main class="canvas">

  <!-- Front, plain -->
  <svg class="card card--front-plain" width="540" height="315" viewBox="0 0 488 285" aria-label="Business card front">
    <rect width="488" height="285" fill="var(--paper)"/>
    <g class="hand">
      <text class="perk perk--accent" transform="rotate(-90 96 145)" x="96" y="145">• WE COME</text>
      <text class="perk perk--accent" transform="rotate(-90 118 145)" x="118" y="145">TO YOU</text>
      <text class="perk perk--plain" transform="rotate(-90 139 145)" x="139" y="145">• ONLY</text>
      <text class="perk perk--plain" transform="rotate(-90 161 145)" x="161" y="145">$49/HR</text>
      <text class="perk perk--accent" transform="rotate(-90 182 145)" x="182" y="145">• NO</text>
      <text class="perk perk--accent" transform="rotate(-90 204 145)" x="204" y="145">CONTRACT,</text>
      <text class="perk perk--plain" transform="rotate(-90 226 145)" x="226" y="145">• NO MONTHLY</text>
      <text class="perk perk--plain" transform="rotate(-90 247 145)" x="247" y="145">FEE</text>
      <text class="perk perk--accent" transform="rotate(-90 269 145)" x="269" y="145">• SOFTWARE</text>
      <text class="perk perk--accent" transform="rotate(-90 290 145)" x="290" y="145">ENGINEER ON</text>
      <text class="perk perk--accent" transform="rotate(-90 312 145)" x="312" y="145">STAFF</text>
      <text class="perk perk--plain" transform="rotate(-90 334 145)" x="334" y="145">• REMOTE</text>
      <text class="perk perk--plain" transform="rotate(-90 355 145)" x="355" y="145">ASSISTANCE</text>
      <text class="perk perk--plain" transform="rotate(-90 377 145)" x="377" y="145">OR VISIT IN</text>
      <text class="perk perk--plain" transform="rotate(-90 398 145)" x="398" y="145">YOUR OFFICE</text>
    </g>
    <text class="wordmark" x="80" y="189" textLength="325" lengthAdjust="spacingAndGlyphs">GEARFIXPRO.ZONE</text>
    <text class="contact-name" x="80" y="249">prename name</text>
    <text class="contact-line" x="211" y="249">email: name.name@postbox.net</text>
    <text class="contact-line" x="211" y="267">mobile: 01470 555 218</text>
  </svg>

  <!-- Front, skyline -->
  <svg class="card card--front-skyline skyline" width="540" height="315" viewBox="0 0 488 285" aria-label="Business card front with skyline blocks">
    <rect width="488" height="285" fill="var(--paper)"/>
    <g class="skyline-blocks">
      <rect class="skyline-block" x="75"    y="59"  width="22" height="91"/>
      <rect class="skyline-block" x="96.5"  y="79"  width="22" height="71"/>
      <rect class="skyline-block" x="118"   y="85"  width="22" height="65"/>
      <rect class="skyline-block" x="139.5" y="77"  width="22" height="73"/>
      <rect class="skyline-block" x="161"   y="107" width="22" height="43"/>
      <rect class="skyline-block" x="182.5" y="49"  width="22" height="101"/>
      <rect class="skyline-block" x="204"   y="20"  width="22" height="130"/>
      <rect class="skyline-block" x="225.5" y="107" width="22" height="43"/>
      <rect class="skyline-block" x="247"   y="27"  width="22" height="123"/>
      <rect class="skyline-block" x="268.5" y="27"  width="22" height="123"/>
      <rect class="skyline-block" x="290"   y="92"  width="22" height="58"/>
      <rect class="skyline-block" x="311.5" y="62"  width="22" height="88"/>
      <rect class="skyline-block" x="333"   y="32"  width="22" height="118"/>
      <rect class="skyline-block" x="354.5" y="47"  width="22" height="103"/>
      <rect class="skyline-block" x="376"   y="37"  width="22" height="113"/>
    </g>
    <g class="hand">
      <text class="perk perk--accent" transform="rotate(-90 90 146)" x="90" y="146">• WE COME</text>
      <text class="perk perk--accent" transform="rotate(-90 111.5 146)" x="111.5" y="146">TO YOU</text>
      <text class="perk perk--plain" transform="rotate(-90 133 146)" x="133" y="146">• ONLY</text>
      <text class="perk perk--plain" transform="rotate(-90 154.5 146)" x="154.5" y="146">$49/HR</text>
      <text class="perk perk--accent" transform="rotate(-90 176 146)" x="176" y="146">• NO</text>
      <text class="perk perk--accent" transform="rotate(-90 197.5 146)" x="197.5" y="146">CONTRACT,</text>
      <text class="perk perk--plain" transform="rotate(-90 219 146)" x="219" y="146">• NO MONTHLY</text>
      <text class="perk perk--plain" transform="rotate(-90 240.5 146)" x="240.5" y="146">FEE</text>
      <text class="perk perk--accent" transform="rotate(-90 262 146)" x="262" y="146">• SOFTWARE</text>
      <text class="perk perk--accent" transform="rotate(-90 283.5 146)" x="283.5" y="146">ENGINEER ON</text>
      <text class="perk perk--accent" transform="rotate(-90 305 146)" x="305" y="146">STAFF</text>
      <text class="perk perk--plain" transform="rotate(-90 326.5 146)" x="326.5" y="146">• REMOTE</text>
      <text class="perk perk--plain" transform="rotate(-90 348 146)" x="348" y="146">ASSISTANCE</text>
      <text class="perk perk--plain" transform="rotate(-90 369.5 146)" x="369.5" y="146">OR VISIT IN</text>
      <text class="perk perk--plain" transform="rotate(-90 391 146)" x="391" y="146">YOUR OFFICE</text>
    </g>
    <text class="wordmark" x="78" y="191" textLength="325" lengthAdjust="spacingAndGlyphs">GEARFIXPRO.ZONE</text>
    <text class="contact-name" x="78" y="249">prename name</text>
    <text class="contact-line" x="209" y="249">email: name.name@postbox.net</text>
    <text class="contact-line" x="209" y="267">mobile: 01470 555 218</text>
  </svg>

  <!-- Back, services -->
  <svg class="card card--back" width="541" height="315" viewBox="0 0 489 285" aria-label="Business card back listing services">
    <rect width="489" height="285" fill="var(--slate)"/>
    <g class="service-cloud">
      <text class="service service--wide" x="67" y="54">SOFTWARE</text>
      <text class="service service--wide" x="67" y="77">INSTALLATION</text>

      <text class="service service--orange" font-size="15" transform="rotate(-90 226 75)" x="226" y="75">Server</text>
      <text class="service service--orange" font-size="15" transform="rotate(-90 243 50)" x="243" y="50">setup</text>

      <text class="service service--light" transform="rotate(-90 266 52)" x="266" y="52">HIPAA</text>
      <text class="service service--light" transform="rotate(-90 285 75)" x="285" y="75">compliance</text>
      <text class="service service--light" transform="rotate(-90 303 60)" x="303" y="60">review and</text>
      <text class="service service--light" transform="rotate(-90 321 75)" x="321" y="75">setup</text>

      <text class="service service--black" x="330" y="58">Wireless</text>
      <text class="service service--black" x="330" y="76">network setup</text>

      <text class="wordmark wordmark--back" x="67" y="125" textLength="370" lengthAdjust="spacingAndGlyphs">GEARFIXPRO.ZONE</text>

      <text class="service service--greythin" transform="rotate(-90 77 185)" x="77" y="185">Website</text>
      <text class="service service--greythin" transform="rotate(-90 97 213)" x="97" y="213">management</text>

      <text class="service service--orange" font-size="15" transform="rotate(-90 121 267)" x="121" y="267">PRINTER SETUP</text>

      <text class="service service--blackb" x="134" y="155">Network</text>
      <text class="service service--blackb" x="134" y="173">troubleshooting</text>
      <text class="service service--grey" x="134" y="193">Disaster</text>
      <text class="service service--grey" x="134" y="212">recovery</text>

      <text class="service service--orange" font-size="13.5" transform="rotate(-90 270 215)" x="270" y="215">Any other</text>
      <text class="service service--orange" font-size="13.5" transform="rotate(-90 289 235)" x="289" y="235">technology</text>
      <text class="service service--orange" font-size="13.5" transform="rotate(-90 307 257)" x="307" y="257">related support</text>
      <text class="service service--black" transform="rotate(-90 322 267)" x="322" y="267">Secure backup setup</text>

      <text class="service service--orange" font-size="14" x="332" y="155">Wired network</text>
      <text class="service service--orange" font-size="14" x="332" y="173">setup</text>
      <text class="service service--black" x="332" y="191">Email setup</text>
    </g>
  </svg>

</main>
</body>
</html>
```